Quorvane - corporate Business Card

We need a good look and innovative business card for a new start up company based in Los Angeles called "Quorvane". We are in a payment business, including payment card, app, and ewallet. We are expert in online payment and Card not present (CNP) transaction.
We need an innovative, modern business card.

Our logo font is Aero Matics

Target Market(s)

Startup - Bank - Online Payment - Card Manufacturing

Industry/Entity Type

Startup

Contact Information for Business Card

phone: 424 555 0173 - Address: 4270 Marbrook blvd, Vellmont City, CA 90418

Requirements
Must have
• Message: innovative, professional, expert, high tech, trust, online payment expert, security
Nice to have
• no comment
Should not have
• no Comment

```html
<!DOCTYPE html>
<html lang="en">
<head>
<meta charset="utf-8">
<title>Quorvane – Business Card</title>
<link rel="stylesheet" href="https://fonts.googleapis.com/css2?family=Lato:wght@400;700&display=swap">
<style>
  :root {
    --brand-red: #b01e2c;
    --card-black: #1d1a1b;
    --card-white: #ffffff;
    --text-grey: #6b6b6b;
    --ghost: #f4ece9;
    --backdrop: #d9d9db;
  }
  * { margin: 0; padding: 0; box-sizing: border-box; }
  html, body { width: 1200px; height: 900px; overflow: hidden; }
  body {
    background: var(--backdrop);
    font-family: "Lato", sans-serif;
    display: flex;
    flex-direction: column;
    align-items: center;
    justify-content: center;
    gap: 60px;
  }
  .card {
    position: relative;
    width: 700px;
    height: 370px;
    border-radius: 22px;
    overflow: hidden;
    box-shadow: 0 10px 30px rgba(0,0,0,.18);
  }
  .brand {
    display: flex;
    align-items: center;
    gap: 18px;
  }
  .brand-dot {
    border-radius: 50%;
    background: var(--brand-red);
    flex: none;
  }
  .brand-name {
    font-weight: 700;
    color: var(--brand-red);
    letter-spacing: 1px;
    line-height: 1;
  }

  /* Front */
  .card-front {
    background: var(--card-black);
    display: flex;
    flex-direction: column;
    align-items: center;
    justify-content: center;
  }
  .card-front .brand-dot { width: 96px; height: 96px; }
  .card-front .brand-name { font-size: 74px; }
  .front-web {
    position: absolute;
    bottom: 58px;
    left: 0; right: 0;
    text-align: center;
    color: #ffffff;
    font-size: 15px;
    letter-spacing: .5px;
  }

  /* Back */
  .card-back { background: var(--card-white); }
  .ghost-circle {
    position: absolute;
    right: -70px;
    top: 110px;
    width: 300px;
    height: 300px;
    border-radius: 50%;
    background: var(--ghost);
  }
  .card-back .brand {
    position: absolute;
    left: 56px;
    top: 110px;
  }
  .card-back .brand-dot { width: 70px; height: 70px; }
  .card-back .brand-name { font-size: 54px; }
  .person {
    position: absolute;
    right: 70px;
    top: 46px;
    text-align: right;
  }
  .person-name { color: var(--brand-red); font-size: 22px; }
  .person-role { color: #222; font-size: 14px; margin-top: 2px; }
  .contact {
    position: absolute;
    left: 56px;
    top: 212px;
    color: var(--text-grey);
    font-size: 14px;
    line-height: 1.45;
  }
  .contact-label { color: var(--brand-red); }
  .contact-list { list-style: none; margin-top: 12px; }
  .contact-list li { display: flex; align-items: center; gap: 10px; }
  .contact-list svg { width: 13px; height: 13px; fill: var(--brand-red); flex: none; }
</style>
</head>
<body>

  <section class="card card-front" aria-label="Card front">
    <div class="brand">
      <span class="brand-dot"></span>
      <span class="brand-name">quorvane</span>
    </div>
    <p class="front-web">www.quorvane.com</p>
  </section>

  <section class="card card-back" aria-label="Card back">
    <div class="ghost-circle"></div>
    <div class="person">
      <p class="person-name">Adrien Caldwell</p>
      <p class="person-role">President</p>
    </div>
    <div class="brand">
      <span class="brand-dot"></span>
      <span class="brand-name">quorvane</span>
    </div>
    <div class="contact">
      <p class="contact-label">Address:</p>
      <p>4270 Marbrook blvd<br>Vellmont City, CA 90418</p>
      <ul class="contact-list">
        <li>
          <svg viewBox="0 0 24 24" aria-hidden="true"><path d="M6.6 10.8a15.1 15.1 0 0 0 6.6 6.6l2.2-2.2a1 1 0 0 1 1-.25 11.4 11.4 0 0 0 3.6.57 1 1 0 0 1 1 1V20a1 1 0 0 1-1 1A17 17 0 0 1 3 4a1 1 0 0 1 1-1h3.5a1 1 0 0 1 1 1c0 1.25.2 2.45.57 3.57a1 1 0 0 1-.25 1z"/></svg>
          424 555 0173
        </li>
        <li>
          <svg viewBox="0 0 24 24" aria-hidden="true"><path d="M2 5h20v14H2z M2 5l10 8 10-8" fill="none" stroke="#b01e2c" stroke-width="2.4"/></svg>
          info@quorvane.com
        </li>
        <li>
          <svg viewBox="0 0 24 24" aria-hidden="true"><circle cx="12" cy="12" r="10" fill="none" stroke="#b01e2c" stroke-width="2"/><path d="M2 12h20M12 2c3 3 3 17 0 20M12 2c-3 3-3 17 0 20" fill="none" stroke="#b01e2c" stroke-width="1.6"/></svg>
          www.quorvane.com
        </li>
      </ul>
    </div>
  </section>

</body>
</html>
```